Tech Company requires UI design for mobile app

We need a mobile app design for a company based in Singapore called "Valdor Systems". We develop innovative Android/iOS business applications. KelmaRun - a collaboration tool targeted at SMEs that improves reporting and communication between different departments of an organisation. We would like to see designs that use the colour orange, our corporate colour. The final design should communicate clean and technology inclined design.

You are expected to recreate the icons, layout and structure without affecting the workflow.This is a workplace app for employee on mobile. The mobile app aims to empower individual employee to complete the following processes:

1. HR processes - taking attendance, timesheet, employment management to payslip)
2. Inventory management - stock taking, gift redemption and real-time stock management
3. Digital form - application for inspection, safety, procurement or request creation)
4. Job - an app that allows web portal to assign work to individual worker.
Updates

Project Deadline Extended
Reason: Received feedback to extens timeline. Cheers!

Target Market(s)

C-Executive, office employee, retail promoter, worker

Industry/Entity Type

Business

Colors

Designer to choose colors to be used in the design.

Requirements
Must have
• - Design must be neat, looks professional and perceived to be user-friendly
• - Use colour theme for each category
• - Must complement with KelmaRun logo them (already attached)
• - Have "apple" feel
• - We like the layout reference 1 & reference 2 photo. However, we prefer a better colour theme (Already Attached)
• - Please download the link for the work required
• https://files.quorvex.com/open?id=7Hq2LmPzXr4WtYb9NcKd3VfJsEa
Nice to have
• More info to follow shortly
Should not have
• - Must not be loud, flashy, dull, bored,
• - Design should not clash with Kelma Run Logo
• -

```html
<!DOCTYPE html>
<html lang="en">
<head>
<meta charset="utf-8">
<title>KelmaRun – Home</title>
<link rel="stylesheet" href="https://fonts.googleapis.com/css2?family=Inter:wght@400;500;600;700&display=swap">
<style>
  :root {
    --orange: #ff9500;
    --bg-page: #e9e9ee;
    --surface: #ffffff;
    --group-bg: #efeff4;
    --tab-bg: #f7f7f7;
    --text: #111111;
    --text-muted: #8e8e93;
    --text-faint: #c3c3c8;
    --divider: #dcdce1;
    --chevron: #b4b4b9;
  }
  * { box-sizing: border-box; margin: 0; padding: 0; }
  html, body { width: 1200px; height: 1200px; overflow: hidden; }
  body {
    background: var(--bg-page);
    font-family: "Inter", sans-serif;
    color: var(--text);
    position: relative;
  }
  .screen {
    position: absolute;
    left: 276px; top: 23px;
    width: 648px; height: 1154px;
    background: var(--group-bg);
    overflow: hidden;
  }
  .status-bar {
    height: 32px;
    background: var(--surface);
    display: flex; align-items: center; justify-content: space-between;
    padding: 0 10px;
    font-size: 20px; font-weight: 500;
    position: relative;
  }
  .status-bar .time { position: absolute; left: 0; right: 0; text-align: center; }
  .status-bar .left, .status-bar .right { display: flex; align-items: center; gap: 6px; }
  .profile-header {
    background: var(--surface);
    height: 277px;
    position: relative;
    border-bottom: 2px solid var(--divider);
  }
  .app-title {
    position: absolute; left: 0; right: 0; top: 60px;
    text-align: center;
    font-size: 57px; font-weight: 700;
    color: var(--orange);
    line-height: 1;
    letter-spacing: -0.5px;
  }
  .avatar {
    position: absolute; left: 25px; top: 124px;
    width: 128px; height: 128px; border-radius: 50%;
    background: radial-gradient(circle at 50% 40%, #c9c2bb 0%, #8c8580 55%, #3a3a40 100%);
  }
  .avatar-badge {
    position: absolute; left: 118px; top: 214px;
    width: 34px; height: 34px; border-radius: 50%;
    background: var(--orange);
    border: 2px solid var(--surface);
    color: #fff; font-size: 21px; font-weight: 500;
    display: flex; align-items: center; justify-content: center;
  }
  .employee-name {
    position: absolute; left: 180px; top: 143px;
    font-size: 28px; font-weight: 500; color: var(--text-muted);
  }
  .employee-id {
    position: absolute; left: 180px; top: 186px;
    font-size: 25px; color: var(--text-faint);
  }
  .section-label {
    height: 61px;
    padding: 0 26px;
    display: flex; align-items: center;
    font-size: 20px; color: var(--text-muted);
    letter-spacing: 0.5px;
    border-bottom: 1px solid var(--divider);
  }
  .menu-list { list-style: none; background: var(--surface); border-bottom: 1px solid var(--divider); }
  .menu-item {
    height: 76px;
    display: flex; align-items: center;
    padding-left: 26px; padding-right: 24px;
    position: relative;
    font-size: 28px;
  }
  .menu-item + .menu-item::before {
    content: ""; position: absolute; left: 0; right: 0; top: 0;
    border-top: 1px solid var(--divider);
  }
  .menu-item .icon { width: 38px; height: 38px; margin-right: 17px; flex: none; }
  .menu-item .label { flex: 1; }
  .menu-item .chevron { width: 14px; height: 24px; }
  .tab-bar {
    position: absolute; left: 0; right: 0; bottom: 0;
    height: 77px;
    background: var(--tab-bg);
    border-top: 1px solid #e6e6ea;
  }
  .tab-bar svg { position: absolute; top: 19px; width: 42px; height: 42px; }
</style>
</head>
<body>
  <main class="screen">
    <div class="status-bar">
      <div class="left">
        <svg width="30" height="16" viewBox="0 0 30 16" fill="#000">
          <rect x="0" y="10" width="4" height="6" rx="1"/><rect x="6" y="7" width="4" height="9" rx="1"/>
          <rect x="12" y="4" width="4" height="12" rx="1"/><rect x="18" y="1" width="4" height="15" rx="1"/>
        </svg>
        <svg width="22" height="16" viewBox="0 0 22 16" fill="none" stroke="#000" stroke-width="2.4" stroke-linecap="round">
          <path d="M2 6a13 13 0 0 1 18 0"/><path d="M5.5 9.5a8 8 0 0 1 11 0"/><circle cx="11" cy="13.5" r="1.5" fill="#000" stroke="none"/>
        </svg>
      </div>
      <span class="time">9:41 AM</span>
      <div class="right">
        <svg width="12" height="18" viewBox="0 0 12 18" fill="none" stroke="#000" stroke-width="1.8"><path d="M1 5l9 8-4 4V1l4 4-9 8"/></svg>
        <span>100%</span>
        <svg width="40" height="18" viewBox="0 0 40 18">
          <rect x="1" y="1" width="34" height="16" rx="3" fill="none" stroke="#000" stroke-width="1.4"/>
          <rect x="3" y="3" width="30" height="12" rx="2" fill="#000"/>
          <rect x="36" y="6" width="2.5" height="6" rx="1" fill="#000"/>
        </svg>
      </div>
    </div>

    <header class="profile-header">
      <h1 class="app-title">KelmaRun</h1>
      <div class="avatar" role="img" aria-label="Employee profile photo"></div>
      <div class="avatar-badge">2</div>
      <p class="employee-name">Rafiq Halden</p>
      <p class="employee-id">EM1104</p>
    </header>

    <div class="section-label">ATTENDANCE</div>
    <ul class="menu-list">
      <li class="menu-item">
        <svg class="icon" viewBox="0 0 38 38"><path d="M19 3a10 10 0 0 0-10 10c0 8 10 21 10 21s10-13 10-21A10 10 0 0 0 19 3z" fill="var(--orange)"/><circle cx="19" cy="13" r="4" fill="#fff"/></svg>
        <span class="label">Take Attendance</span>
        <svg class="chevron" viewBox="0 0 14 24" fill="none" stroke="var(--chevron)" stroke-width="2.4" stroke-linecap="round"><path d="M3 3l9 9-9 9"/></svg>
      </li>
      <li class="menu-item">
        <svg class="icon" viewBox="0 0 38 38"><circle cx="19" cy="19" r="18" fill="var(--orange)"/><path d="M19 8v11h-7" fill="none" stroke="#fff" stroke-width="2.8" stroke-linecap="round"/></svg>
        <span class="label">Today</span>
        <svg class="chevron" viewBox="0 0 14 24" fill="none" stroke="var(--chevron)" stroke-width="2.4" stroke-linecap="round"><path d="M3 3l9 9-9 9"/></svg>
      </li>
      <li class="menu-item">
        <svg class="icon" viewBox="0 0 38 38"><rect x="1" y="3" width="36" height="32" rx="3" fill="var(--orange)"/><rect x="4" y="11" width="30" height="21" fill="#fff"/><g stroke="var(--orange)" stroke-width="2"><path d="M7 16h24M7 21h24M7 26h24"/></g></svg>
        <span class="label">Past Records</span>
        <svg class="chevron" viewBox="0 0 14 24" fill="none" stroke="var(--chevron)" stroke-width="2.4" stroke-linecap="round"><path d="M3 3l9 9-9 9"/></svg>
      </li>
      <li class="menu-item">
        <svg class="icon" viewBox="0 0 38 38"><circle cx="19" cy="19" r="18" fill="var(--orange)"/><g fill="#fff"><circle cx="12" cy="15" r="3.5"/><circle cx="26" cy="15" r="3.5"/><circle cx="19" cy="13" r="4"/><path d="M6 26c0-4 3-6 6-6s6 2 6 6zM20 26c0-4 3-6 6-6s6 2 6 6zM12 27c0-5 3-8 7-8s7 3 7 8z"/></g></svg>
        <span class="label">Station</span>
        <svg class="chevron" viewBox="0 0 14 24" fill="none" stroke="var(--chevron)" stroke-width="2.4" stroke-linecap="round"><path d="M3 3l9 9-9 9"/></svg>
      </li>
    </ul>

    <nav class="tab-bar">
      <svg style="left:25px" viewBox="0 0 42 42"><path d="M21 5L3 21h5v16h10V27h6v10h10V21h5z" fill="var(--orange)"/></svg>
      <svg style="left:209px" viewBox="0 0 42 42" fill="none" stroke="var(--orange)" stroke-width="2.4"><circle cx="21" cy="21" r="18"/><circle cx="21" cy="16" r="6" fill="var(--orange)"/><path d="M9 33c3-6 7-8 12-8s9 2 12 8" fill="var(--orange)"/></svg>
      <svg style="left:396px" viewBox="0 0 42 42"><rect x="3" y="5" width="36" height="32" rx="2" fill="none" stroke="var(--orange)" stroke-width="2"/><rect x="3" y="5" width="36" height="8" fill="var(--orange)"/><g fill="var(--orange)"><rect x="8" y="18" width="3" height="3"/><rect x="14" y="18" width="3" height="3"/><rect x="20" y="18" width="3" height="3"/><rect x="26" y="18" width="3" height="3"/><rect x="32" y="18" width="3" height="3"/><rect x="8" y="24" width="3" height="3"/><rect x="14" y="24" width="3" height="3"/><rect x="20" y="24" width="3" height="3"/><rect x="26" y="24" width="3" height="3"/><rect x="32" y="24" width="3" height="3"/><rect x="8" y="30" width="3" height="3"/><rect x="14" y="30" width="3" height="3"/><rect x="20" y="30" width="3" height="3"/></g></svg>
      <svg style="left:580px" viewBox="0 0 42 42" fill="none" stroke="var(--orange)" stroke-width="2.4" stroke-linecap="round"><path d="M6 18A15 15 0 0 1 34 14"/><path d="M36 24A15 15 0 0 1 8 28"/><path d="M34 6v8h-8" /><path d="M8 36v-8h8"/></svg>
    </nav>
  </main>
</body>
</html>
```